Lindenfield Advocacy Learning Forums
Icon Set
We wish to design an icon set to be used in printed brochures as well as our website and other marketing materials.
Law
Professional - Lawyers. LALF provides legal training and education seminar for lawyers.
LALF organises and presents regular legal professional seminars throughout Australia. Our marketing is heavily based on direct mail. When we schedule our seminars we design and print brochures and send them to all lawyers that are close to the location of the seminars.
All lawyers in Australia are required to attend a specified number of hours of continuing education seminars each year. For every hour of attendance, they can gain 1 point and they usually need to accumulate 10-20 points per year.
In most cases there are also compulsory areas that must be covered. Each State has different requirements, but there are four main compulsory areas:
1. Legal Ethics
2. Practice Management or Business Skills
3. Professional Skills
4. Substantive Law
There is also an additional subject area which is used in one location (Sydney) – this is for OH & S, Employment Law, Equal Opportunity and Discrimination Law.
We always designate how many points (or hours) a lawyer will get by attending one of our seminars and in which compulsory area they will get the points.
What we need is an icon for each of the four main areas. Each icon should ideally be recognizable with the particular compulsory area and be a different colour. We would also like an icon for the additional subject area in Sydney, but this is not essential.
Also, it would be ideal if the points and/or description of the compulsory area could be incorporated within the icon graphic. However, if this is not possible, then this can be done as text under the icon or to the side.
The icon does not need to be any particular size – it could be square, round, rectangle or anything else. But, please remember the context we will be using it in. The main use will be in the marketing brochures. But we would also like to use it on our website and other media as required.
I will also need to be able to edit each icon as the descriptions of the compulsory subjects differ slightly between the States. I will also need to be able to change the number of points. Ideally, I should be able to edit the icons using Adobe Illustrator.
I will upload several examples of our marketing brochures which show how we currently designate points/compulsory areas for each seminar. The icons we use at the moment are a set of stock-icons I purchased on the web. However, these icons were never ideal and we would like something that is specifically designed for our purposes.
Also, if you look at the back panel of each brochure (panel 5 on the first page), there is a description of what each icon represents and more information on the compulsory subjects. This information is different for each State.
I will also upload some examples of icons used by some of our competitors. Please note that none of these examples actually specify the number of points within the graphic. This is not ideal. I think a clear number should be included in the graphic. For example, if the seminar has 3 points – then a clear “3” should stand out in the icon.
Finally, please also note that I wish to redesign the template we use for our marketing brochures. I will create a separate project for this, but you may wish to consider submitting a design for this as well. Please see this project for the specific details.
Example of Sydney Brochure
Example of Melbourne Brochure
Example of Brisbane Brochure
Example of Perth Brochure

```html
<!DOCTYPE html>
<html lang="en">
<head>
<meta charset="utf-8">
<title>CPD Compulsory Area Icon Set</title>
<link href="https://fonts.googleapis.com/css2?family=Source+Sans+3:wght@400;600&display=swap" rel="stylesheet">
<style>
  :root {
    --ethics-light: #5cc2f2;
    --ethics: #1f95da;
    --ethics-dark: #0f73b8;
    --practice-light: #f2845a;
    --practice: #e4572b;
    --practice-dark: #c7401a;
    --skills-light: #6cc96f;
    --skills: #3ba84a;
    --skills-dark: #238a35;
    --law-light: #c964b4;
    --law: #a62a8e;
    --law-dark: #861a72;
    --frame: #cfd3d7;
    --frame-inner: #f4f5f6;
    --ink-light: #ffffff;
    --page: #ffffff;
  }
  * { box-sizing: border-box; margin: 0; padding: 0; }
  html, body {
    width: 1200px; height: 871px; overflow: hidden;
    background: var(--page);
    font-family: "Source Sans 3", "Myriad Pro", Arial, sans-serif;
  }
  .icon-set { position: relative; width: 1200px; height: 871px; }
  .area-row {
    position: absolute; left: 58px; height: 118px;
    display: flex; gap: 14px; align-items: stretch;
  }
  .area-row.ethics   { top: 110px; --c-light: var(--ethics-light);   --c: var(--ethics);   --c-dark: var(--ethics-dark); }
  .area-row.practice { top: 286px; --c-light: var(--practice-light); --c: var(--practice); --c-dark: var(--practice-dark); }
  .area-row.skills   { top: 461px; --c-light: var(--skills-light);   --c: var(--skills);   --c-dark: var(--skills-dark); }
  .area-row.law      { top: 636px; --c-light: var(--law-light);      --c: var(--law);      --c-dark: var(--law-dark); }

  .tile, .label-bar {
    border: 3px solid var(--frame);
    border-radius: 9px;
    background: var(--frame-inner);
    padding: 4px;
    box-shadow: 0 1px 2px rgba(0,0,0,.12);
  }
  .tile { width: 118px; }
  .tile-face, .bar-face {
    width: 100%; height: 100%;
    border-radius: 5px;
    background: linear-gradient(180deg, var(--c-light) 0%, var(--c) 48%, var(--c-dark) 52%, var(--c) 100%);
    position: relative; overflow: hidden;
  }
  .tile-face svg { position: absolute; inset: 10px; width: calc(100% - 20px); height: calc(100% - 20px); }
  .pictogram-slot {
    position: absolute; inset: 16px;
    border-radius: 6px;
    background: rgba(255,255,255,.32);
  }
  .label-bar { width: 812px; margin-left: 8px; }
  .bar-face { display: flex; align-items: flex-end; }
  .area-name {
    flex: 1;
    color: var(--ink-light);
    font-size: 37px; font-weight: 400;
    padding: 0 0 14px 18px;
    line-height: 1;
    letter-spacing: .2px;
  }
  .points-box {
    align-self: stretch;
    width: 212px;
    margin: 6px 6px 6px 0;
    border-radius: 4px;
    background: linear-gradient(180deg, rgba(255,255,255,.28) 0%, rgba(255,255,255,.12) 48%, rgba(0,0,0,.12) 52%, rgba(0,0,0,.06) 100%);
    color: var(--ink-light);
    display: flex; flex-direction: column; align-items: center; justify-content: center;
    line-height: 1.05;
  }
  .points-value { font-size: 31px; font-weight: 400; }
  .points-unit { font-size: 22px; font-weight: 400; }
</style>
</head>
<body>
<main class="icon-set">

  <section class="area-row ethics">
    <div class="tile"><div class="tile-face">
      <svg viewBox="0 0 100 100" aria-label="Book icon">
        <path d="M12 34 L62 14 L90 52 L40 74 Z" fill="#fff"/>
        <path d="M12 34 L40 74 L40 84 L12 44 Z" fill="#e6f3fb"/>
        <path d="M40 74 L90 52 L90 62 L40 84 Z" fill="#d2e9f7"/>
        <path d="M18 42 L44 80" stroke="var(--ethics-dark)" stroke-width="2"/>
      </svg>
    </div></div>
    <div class="tile"><div class="tile-face">
      <svg viewBox="0 0 100 100" aria-label="Scales of justice icon">
        <g fill="#fff">
          <rect x="47" y="16" width="6" height="62"/>
          <circle cx="50" cy="15" r="5"/>
          <rect x="16" y="24" width="68" height="5" rx="2"/>
          <path d="M20 29 L10 56 L30 56 Z M80 29 L70 56 L90 56 Z" fill="none" stroke="#fff" stroke-width="2"/>
          <path d="M8 56 Q20 70 32 56 Z"/>
          <path d="M68 56 Q80 70 92 56 Z"/>
          <path d="M34 86 Q50 72 66 86 Z"/>
        </g>
      </svg>
    </div></div>
    <div class="label-bar"><div class="bar-face">
      <span class="area-name">Legal Ethics</span>
      <div class="points-box"><span class="points-value">3.25</span><span class="points-unit">CPD Points</span></div>
    </div></div>
  </section>

  <section class="area-row practice">
    <div class="tile"><div class="tile-face">
      <div class="pictogram-slot" role="img" aria-label="Handshake pictogram"></div>
    </div></div>
    <div class="tile"><div class="tile-face">
      <div class="pictogram-slot" role="img" aria-label="Two business people pictogram"></div>
    </div></div>
    <div class="label-bar"><div class="bar-face">
      <span class="area-name">Practice Management</span>
      <div class="points-box"><span class="points-value">3.25</span><span class="points-unit">CPD Points</span></div>
    </div></div>
  </section>

  <section class="area-row skills">
    <div class="tile"><div class="tile-face">
      <svg viewBox="0 0 100 100" aria-label="Pen nib icon">
        <path d="M16 84 L30 44 L62 20 L82 40 L58 72 Z" fill="#fff"/>
        <path d="M16 84 L44 56" stroke="var(--skills-dark)" stroke-width="3"/>
        <circle cx="47" cy="53" r="5" fill="var(--skills-dark)"/>
        <path d="M60 14 L88 42 L82 48 L54 20 Z" fill="#fff"/>
      </svg>
    </div></div>
    <div class="tile"><div class="tile-face">
      <svg viewBox="0 0 100 100" aria-label="Briefcase icon">
        <path d="M36 32 V22 Q36 18 40 18 H60 Q64 18 64 22 V32 H58 V24 H42 V32 Z" fill="#fff"/>
        <rect x="12" y="32" width="76" height="48" rx="4" fill="#fff"/>
        <rect x="12" y="52" width="76" height="3" fill="var(--skills-dark)"/>
        <rect x="45" y="48" width="10" height="10" rx="1" fill="#fff" stroke="var(--skills-dark)" stroke-width="2"/>
      </svg>
    </div></div>
    <div class="label-bar"><div class="bar-face">
      <span class="area-name">Professional Skills</span>
      <div class="points-box"><span class="points-value">3.25</span><span class="points-unit">CPD Points</span></div>
    </div></div>
  </section>

  <section class="area-row law">
    <div class="tile"><div class="tile-face">
      <svg viewBox="0 0 100 100" aria-label="Gavel icon">
        <g fill="#fff">
          <g transform="rotate(-40 50 40)">
            <rect x="30" y="20" width="40" height="20" rx="3"/>
            <rect x="46" y="40" width="8" height="46" rx="2"/>
          </g>
          <rect x="50" y="78" width="38" height="6" rx="1"/>
          <rect x="46" y="84" width="46" height="6" rx="1"/>
        </g>
      </svg>
    </div></div>
    <div class="tile"><div class="tile-face">
      <div class="pictogram-slot" role="img" aria-label="Judge in wig pictogram"></div>
    </div></div>
    <div class="label-bar"><div class="bar-face">
      <span class="area-name">Substantive Law</span>
      <div class="points-box"><span class="points-value">3.25</span><span class="points-unit">CPD Points</span></div>
    </div></div>
  </section>

</main>
</body>
</html>
```